"Dental Kestrel" clinic needs brochure

a creative design is needed for flyer for a dental clinic, all info available on this website www.dentalkestrel.ae, new imagery needed.

Clinic

```html
<!DOCTYPE html>
<html lang="en">
<head>
<meta charset="utf-8">
<title>Dental Kestrel Clinic – Flyer</title>
<link href="https://fonts.googleapis.com/css2?family=Carlito:ital,wght@0,400;0,700;1,400;1,700&display=swap" rel="stylesheet">
<style>
  :root {
    --page: #ffffff;
    --backdrop: #ffffff;
    --cyan: #9cfdfd;
    --royal: #0544fb;
    --teal: #1f7a6c;
    --ink: #111111;
    --card-bg: #e0fdfd;
    --card-border: #a9bdf7;
    --heading-blue: #1f3fe0;
    --map-land: #e9e6df;
    --map-green: #c8ef9a;
  }
  * { box-sizing: border-box; margin: 0; padding: 0; }
  html, body { width: 1200px; height: 1200px; overflow: hidden; background: var(--backdrop); }
  body { font-family: "Carlito", "Calibri", sans-serif; color: var(--ink); }

  .flyer {
    position: absolute; left: 176px; top: 0;
    width: 847px; height: 1200px;
    background: var(--page); overflow: hidden;
  }
  .flyer__shapes { position: absolute; inset: 0; width: 100%; height: 100%; }

  .location-map {
    position: absolute; left: 71px; top: 44px; width: 709px; height: 222px;
    background: linear-gradient(110deg, var(--map-land) 0%, var(--map-land) 68%, var(--map-green) 80%, var(--map-green) 100%);
  }

  .brand {
    position: absolute; left: 70px; top: 292px;
    display: flex; align-items: center; gap: 14px;
  }
  .brand__dot { width: 30px; height: 30px; border-radius: 50%; background: var(--teal); }
  .brand__name { font-size: 34px; font-weight: 700; color: var(--teal); letter-spacing: 1px; }

  .testimonials {
    position: absolute; left: 53px; top: 378px; width: 382px; height: 363px;
    background: var(--card-bg); border: 3px solid var(--card-border); border-radius: 16px;
    padding: 10px 14px 0 9px;
  }
  .testimonials__title {
    font-size: 25px; font-weight: 700; font-style: italic; color: var(--heading-blue);
    margin-left: 6px; margin-bottom: 6px;
  }
  .testimonial { font-style: italic; font-size: 18.5px; line-height: 24px; margin-bottom: 24px; }
  .testimonial__author { display: block; text-align: right; font-weight: 700; }

  .hours {
    position: absolute; left: 495px; top: 744px;
    font-size: 21px; line-height: 27px;
  }
  .hours__title, .address__title { font-size: 23px; font-weight: 700; }

  .address {
    position: absolute; left: 236px; top: 986px;
    font-size: 21px; line-height: 26.7px; color: #ffffff;
  }
</style>
</head>
<body>
  <main class="flyer">
    <svg class="flyer__shapes" viewBox="0 0 1032 1462" preserveAspectRatio="none" aria-hidden="true">
      <polygon points="1032,432 1032,1462 0,1462" fill="var(--cyan)"/>
      <polygon points="516,953 0,1462 1032,1462" fill="var(--royal)"/>
    </svg>

    <div class="location-map" role="img" aria-label="Street map of Abu Dhabi marking the clinic location near the park and university"></div>

    <div class="brand">
      <span class="brand__dot"></span>
      <span class="brand__name">Dental Kestrel</span>
    </div>

    <section class="testimonials">
      <h2 class="testimonials__title">HAPPY CLIENTS</h2>
      <p class="testimonial">“I'm very happy with my new hollywood smile, perfect color, very natural.”
        <span class="testimonial__author">- Layla Haddad</span></p>
      <p class="testimonial">“I barely felt the extraction, the procedure was fast and painless.”
        <span class="testimonial__author">- Omar Nasri</span></p>
      <p class="testimonial">“They took good care of my daughters, they aren't worried about their next clean up at all!!.”
        <span class="testimonial__author">- Anika</span></p>
    </section>

    <section class="hours">
      <h3 class="hours__title">Opening Hours</h3>
      <p>Saturday – Sunday 11 AM –8 PM</p>
      <p>Thursday 11 AM – 4 PM</p>
    </section>

    <section class="address">
      <h3 class="address__title">Our Address</h3>
      <p>Flat 404,</p>
      <p>Al Noor Garden Street,</p>
      <p>Opposite the Civic Centre</p>
      <p>Abu Dhabi,</p>
      <p>&nbsp;Tel: +971 2 555 0142</p>
      <p>www.dentalkestrel.ae</p>
    </section>
  </main>
</body>
</html>
```